Create banners that convert into clicks

I'm looking for a for a banner that with following details.
top slogan:
We Make Your Phone Ring.

ROI Driven SEO & PPC Campaigns.
No Hype! Just Results!

Bottom: Get A Free SEO & PPC Analysis

Image: Picture of phone off hook.
Logos and Colors Attached

Banner Sizes needed:
728x90
300x250
480x60

Reason: Not changes by designers per messages sent. would like at least 2 days.

Target Market(s)

Small To Med Size business owners

Industry/Entity Type

Seo

Requirements
Must have
• Please keep to main color scheme of logo...Blue & White.
May use a bright color to draw attention like yellow or orange or similar.

```html
<!DOCTYPE html>
<html lang="en">
<head>
<meta charset="utf-8">
<title>Brightline Marketing – Banner Set</title>
<link href="https://fonts.googleapis.com/css2?family=Oswald:wght@400;500&display=swap" rel="stylesheet">
<style>
  :root {
    --brand-blue: #3a63b0;
    --bright-blue: #1f74c9;
    --navy: #1f3b73;
    --accent-orange: #f7941d;
    --white: #ffffff;
    --backdrop: #8c8c8c;
    --phone-blue: #3c8fd6;
    --phone-black: #2b2b2b;
  }
  * { margin: 0; padding: 0; box-sizing: border-box; }
  html, body { width: 1200px; height: 636px; overflow: hidden; }
  body {
    background: var(--backdrop);
    font-family: "Oswald", "Arial Narrow", sans-serif;
    position: relative;
  }
  .banner { position: absolute; background: var(--white); overflow: hidden; }
  .banner > * { position: absolute; }
  .brand-name {
    color: var(--brand-blue);
    font-weight: 400;
    text-align: center;
    line-height: 1;
    white-space: nowrap;
  }
  .phone-photo { border-radius: 6px; }

  /* 300x250 medium rectangle */
  .banner-rectangle { left: 87px; top: 71px; width: 374px; height: 311px; }
  .banner-rectangle .brand-name { left: 0; width: 374px; top: 30px; font-size: 34px; }
  .banner-rectangle .slogan { left: 0; width: 374px; top: 88px; text-align: center; color: var(--accent-orange); font-size: 28px; }
  .banner-rectangle .pitch { left: 20px; width: 240px; top: 137px; text-align: center; color: var(--brand-blue); font-size: 23px; line-height: 32px; }
  .banner-rectangle .phone-photo { left: 250px; top: 130px; width: 62px; height: 72px; background: linear-gradient(160deg, #555, var(--phone-black)); }
  .banner-rectangle .wave { left: 0; top: 215px; width: 374px; height: 96px; }
  .banner-rectangle .cta { left: 0; width: 374px; top: 264px; text-align: center; color: var(--white); font-size: 27px; }

  /* 480x60 banner */
  .banner-full { left: 524px; top: 309px; width: 597px; height: 74px; }
  .banner-full .slogan { left: 6px; top: 1px; color: var(--accent-orange); font-size: 18px; }
  .banner-full .phone-photo { left: 4px; top: 30px; width: 100px; height: 40px; background: linear-gradient(160deg, #6fb0e6, var(--phone-blue)); }
  .banner-full .brand-name { left: 118px; width: 235px; top: 34px; font-size: 23px; }
  .banner-full .side-panel { left: 355px; top: 0; width: 242px; height: 74px; }
  .banner-full .pitch { left: 368px; width: 229px; top: 2px; text-align: center; color: var(--white); font-size: 15px; line-height: 21px; }
  .banner-full .cta { left: 368px; width: 229px; top: 46px; text-align: center; color: var(--brand-blue); font-size: 15px; }

  /* 728x90 leaderboard */
  .banner-leaderboard { left: 187px; top: 446px; width: 907px; height: 112px; }
  .banner-leaderboard .side-panel { left: 0; top: 0; width: 170px; height: 112px; }
  .banner-leaderboard .slogan { left: 0; width: 150px; top: 8px; text-align: center; color: var(--white); font-size: 25px; line-height: 32px; }
  .banner-leaderboard .pitch { left: 176px; width: 320px; top: 4px; text-align: center; color: var(--brand-blue); font-size: 25px; line-height: 32px; }
  .banner-leaderboard .cta { left: 176px; width: 320px; top: 72px; text-align: center; color: var(--navy); font-size: 24px; }
  .banner-leaderboard .phone-photo { left: 506px; top: 10px; width: 28px; height: 95px; background: linear-gradient(90deg, #6fb0e6, var(--phone-blue)); }
  .banner-leaderboard .brand-name { left: 550px; width: 350px; top: 36px; font-size: 38px; }
</style>
</head>
<body>

<section class="banner banner-rectangle" aria-label="300 by 250 banner">
  <div class="brand-name">Brightline Marketing</div>
  <p class="slogan">We Make Your Phone Ring</p>
  <p class="pitch">ROI Driven SEO<br>&amp; PPC Campaigns<br>No Hype ! Just Results !</p>
  <div class="phone-photo" role="img" aria-label="Photo of a black rotary telephone with the handset off the hook"></div>
  <svg class="wave" viewBox="0 0 374 96" preserveAspectRatio="none" aria-hidden="true">
    <path d="M0 28 C90 48 200 38 280 14 C320 3 350 0 374 0 L374 96 L0 96 Z" fill="var(--bright-blue)"/>
  </svg>
  <p class="cta">Get A Free SEO &amp; PPC Analysis</p>
</section>

<section class="banner banner-full" aria-label="480 by 60 banner">
  <p class="slogan">We Make Your Phone Ring</p>
  <div class="phone-photo" role="img" aria-label="Photo of a blue telephone handset off the hook"></div>
  <div class="brand-name">Brightline Marketing</div>
  <svg class="side-panel" viewBox="0 0 242 74" preserveAspectRatio="none" aria-hidden="true">
    <path d="M12 0 L242 0 L242 74 L0 74 Z" fill="var(--accent-orange)"/>
  </svg>
  <p class="pitch">ROI Driven SEO &amp; PPC Campaigns<br>No Hype ! Just Results !</p>
  <p class="cta">Get A Free SEO &amp; PPC Analysis</p>
</section>

<section class="banner banner-leaderboard" aria-label="728 by 90 banner">
  <svg class="side-panel" viewBox="0 0 170 112" preserveAspectRatio="none" aria-hidden="true">
    <path d="M0 0 L170 0 L150 112 L0 112 Z" fill="var(--accent-orange)"/>
  </svg>
  <p class="slogan">We Make<br>Your<br>Phone Ring</p>
  <p class="pitch">ROI Driven SEO &amp; PPC Campaigns<br>No Hype ! Just Results !</p>
  <p class="cta">Get A Free SEO &amp; PPC Analysis</p>
  <div class="phone-photo" role="img" aria-label="Photo of a blue telephone handset hanging by its cord"></div>
  <div class="brand-name">Brightline Marketing</div>
</section>

</body>
</html>
```